buseisness card

design a card that similar to my web site
TRELLINGWORKSLLC .COM

Contact Information for Business Card

NAME PHONE # WEBSITE EMAIL AND DISCTIPTION OF WHAT WE DO

Colors
0054AA
0677BA
7BADD7
CADEEF
E8F1F8

Requirements
Must have
• lOGO AND DETAILS
Nice to have
• I LIKE THE WATER LIKE ON MY WEB SITE

```html
<!DOCTYPE html>
<html lang="en">
<head>
<meta charset="utf-8">
<title>Trelling Works – Business Card</title>
<link rel="stylesheet" href="https://fonts.googleapis.com/css2?family=Montserrat:wght@700&family=Roboto:wght@400;500&display=swap">
<style>
  :root {
    --navy: #0054AA;
    --blue: #0677BA;
    --sky: #7BADD7;
    --mist: #CADEEF;
    --foam: #E8F1F8;
    --ink: #555a60;
    --ink-dark: #4a4e54;
    --sea-top: #0d4a5c;
    --sea-mid: #0f7381;
    --sea-deep: #083a4a;
    --backdrop: #2a2b2d;
    --card-white: #ffffff;
  }
  * { margin: 0; padding: 0; box-sizing: border-box; }
  html, body { width: 1200px; height: 929px; overflow: hidden; }
  body {
    background: var(--backdrop);
    position: relative;
    font-family: "Roboto", Arial, sans-serif;
  }
  .card {
    position: absolute;
    width: 620px;
    height: 354px;
    border-radius: 2px;
    overflow: hidden;
    box-shadow: 0 10px 28px rgba(0,0,0,.45);
  }

  /* Front */
  .card-front { left: 110px; top: 80px; }
  .sea-photo {
    position: absolute; inset: 0;
    background:
      radial-gradient(ellipse at 50% 55%, rgba(40,150,160,.55), transparent 60%),
      linear-gradient(180deg, var(--sea-top) 0%, var(--sea-mid) 50%, var(--sea-deep) 100%);
  }
  .front-brand {
    position: absolute; left: 0; right: 0; top: 150px;
    display: flex; align-items: center; justify-content: center; gap: 14px;
  }
  .front-brand .mark-dot {
    width: 30px; height: 30px; border-radius: 50%;
    background: var(--card-white);
  }
  .front-brand .brand-name {
    font-family: "Montserrat", Arial, sans-serif;
    font-weight: 700; font-size: 34px; letter-spacing: 1px;
    color: var(--card-white);
  }

  /* Back */
  .card-back { left: 470px; top: 490px; background: var(--card-white); }
  .pipe-art {
    position: absolute; right: 0; top: 0; width: 300px; height: 354px;
    background: linear-gradient(135deg, var(--foam) 0%, #eef1f4 55%, var(--card-white) 100%);
  }
  .accent-bar {
    position: absolute; left: 0; top: 250px; width: 16px; height: 40px;
    background: var(--blue);
  }
  .details { position: absolute; left: 44px; top: 46px; }
  .brand-name-back {
    font-family: "Montserrat", Arial, sans-serif;
    font-weight: 700; font-size: 25px; color: var(--blue);
    display: flex; align-items: center; gap: 10px;
    margin-bottom: 18px;
  }
  .brand-name-back .mark-dot {
    width: 20px; height: 20px; border-radius: 50%; background: var(--blue);
  }
  .person-name {
    font-family: "Montserrat", Arial, sans-serif;
    font-weight: 700; font-size: 19px; color: var(--blue);
  }
  .person-title {
    font-weight: 500; font-size: 15px; color: var(--ink-dark);
    margin-bottom: 14px;
  }
  .address { font-size: 16px; color: var(--ink); line-height: 1.3; margin-bottom: 8px; }
  .contact-list { list-style: none; }
  .contact-list li {
    display: flex; align-items: center; gap: 10px;
    font-size: 16px; color: var(--ink); line-height: 1.5;
  }
  .contact-list svg { width: 16px; height: 16px; flex: none; }
</style>
</head>
<body>

  <section class="card card-front">
    <div class="sea-photo" role="img" aria-label="Underwater photograph of teal sea water with light rays"></div>
    <div class="front-brand">
      <span class="mark-dot"></span>
      <span class="brand-name">TRELLING WORKS</span>
    </div>
  </section>

  <section class="card card-back">
    <div class="pipe-art" role="img" aria-label="Illustration of grey plumbing pipes with a valve and leaking blue water drops"></div>
    <div class="accent-bar"></div>
    <div class="details">
      <div class="brand-name-back"><span class="mark-dot"></span>TRELLING WORKS</div>
      <div class="person-name">MARCUS HALLORIN</div>
      <div class="person-title">Managing Director</div>
      <p class="address">1840 Riverside Court<br>Dayton, OH 45402</p>
      <ul class="contact-list">
        <li>
          <svg viewBox="0 0 16 16" aria-hidden="true"><path fill="var(--blue)" d="M3.5 1.5l2.5 3-1.5 1.5c.8 1.9 2.1 3.2 4 4l1.5-1.5 3 2.5-1.5 2.5C6.5 13 3 9.5 1 4.5z"/></svg>
          +740 555 0148
        </li>
        <li>
          <svg viewBox="0 0 16 16" aria-hidden="true"><rect x="1" y="3" width="14" height="10" fill="var(--blue)"/><path d="M1.5 3.5L8 9l6.5-5.5" stroke="#fff" stroke-width="1.2" fill="none"/></svg>
          mh@tw208.com
        </li>
        <li>
          <svg viewBox="0 0 16 16" aria-hidden="true"><circle cx="8" cy="8" r="6.5" fill="none" stroke="var(--blue)" stroke-width="1.4"/><ellipse cx="8" cy="8" rx="2.8" ry="6.5" fill="none" stroke="var(--blue)" stroke-width="1.2"/><path d="M1.5 8h13" stroke="var(--blue)" stroke-width="1.2"/></svg>
          www.trellingworksllc.com
        </li>
      </ul>
    </div>
  </section>

</body>
</html>
```